Bauzaun-Banner für Abbruchfirma und Schadstoffsanierung
Zielgruppe
Abbruchfirma und Schadstoffsanierung
Aufgabenstellung
Unsere Logo und die Tätigkeiten die wir anbieten müssen vertreten sein
Wir möchten einen Banner für einen Bauzaun entwickeln lassen. Maße sind 340cm x 173 cm

```html
<!DOCTYPE html>
<html lang="de">
<head>
<meta charset="utf-8">
<title>Brenholt Bauservice – Bauzaun-Banner</title>
<link rel="stylesheet" href="https://fonts.googleapis.com/css2?family=Montserrat:wght@600;800&family=Fira+Sans+Condensed:wght@600&display=swap">
<style>
  :root {
    --bg: #d9dadc;
    --paper: #f1f0ef;
    --ink: #141414;
    --red: #cf1f1b;
    --red-dark: #b51814;
    --white: #ffffff;
    --photo-a: #8a7f76;
    --photo-b: #c9c1b8;
    --photo-c: #4a5b86;
  }
  * { margin: 0; padding: 0; box-sizing: border-box; }
  html, body { width: 1200px; height: 800px; overflow: hidden; background: var(--bg); }
  .banner {
    position: absolute; left: 0; top: 94px;
    width: 1200px; height: 611px;
    background: var(--paper); overflow: hidden;
  }
  .photo {
    position: absolute; left: 420px; top: 0; width: 780px; height: 611px;
    background:
      radial-gradient(ellipse 260px 300px at 230px 330px, var(--photo-c) 0%, rgba(74,91,134,0) 70%),
      linear-gradient(120deg, var(--photo-a) 0%, var(--photo-b) 55%, #e3ddd6 100%);
  }
  .panel { position: absolute; left: 0; top: 0; width: 620px; height: 611px; }
  .brand {
    position: absolute; left: 70px; top: 150px;
    display: flex; align-items: center; gap: 12px;
  }
  .brand-mark { width: 30px; height: 30px; background: var(--red); }
  .brand-name {
    font-family: "Montserrat", sans-serif; font-weight: 600;
    font-size: 34px; color: var(--ink); letter-spacing: .5px;
  }
  .brand-tagline {
    position: absolute; left: 72px; top: 200px;
    font-family: "Montserrat", sans-serif; font-weight: 600;
    font-size: 11px; letter-spacing: 1.4px; color: var(--ink);
  }
  .headline {
    position: absolute; left: 70px; top: 275px;
    font-family: "Montserrat", sans-serif; font-weight: 800;
    font-size: 58px; line-height: 1.12; color: var(--ink);
  }
  .headline .highlight {
    background: var(--red); color: var(--white);
    padding: 0 12px; display: inline-block; line-height: 1.05;
  }
  .web {
    position: absolute; left: 72px; top: 548px;
    font-family: "Montserrat", sans-serif; font-weight: 800;
    font-size: 20px; color: var(--ink);
  }
  .services { position: absolute; right: 0; top: 42px; width: 420px; }
  .service {
    position: relative; margin-left: auto; margin-bottom: 12px;
    background: var(--red);
    clip-path: polygon(34px 0, 100% 0, 100% 100%, 0 100%);
    color: var(--white); text-align: right;
    font-family: "Fira Sans Condensed", sans-serif; font-weight: 600;
    font-size: 38px; line-height: 1.08; padding: 8px 30px 8px 40px;
  }
  .service:nth-child(1) { width: 380px; }
  .service:nth-child(2) { width: 410px; }
  .service:nth-child(3) { width: 400px; }
  .service:nth-child(4) { width: 400px; }
</style>
</head>
<body>
  <main class="banner">
    <div class="photo" role="img" aria-label="Foto: Bauarbeiter mit rotem Helm und blauer Latzhose schlägt mit einem Vorschlaghammer auf eine Ziegelwand"></div>

    <svg class="panel" viewBox="0 0 620 611" aria-hidden="true">
      <path d="M0 0 H555 C610 0 600 40 590 90 C560 260 500 430 440 611 H0 Z" fill="#f1f0ef"/>
    </svg>

    <div class="brand">
      <span class="brand-mark"></span>
      <span class="brand-name">Brenholt Bauservice</span>
    </div>
    <p class="brand-tagline">SCHADSTOFFSANIERUNG | ABBRUCH | ENTSORGUNG</p>

    <h1 class="headline">Wir machen<br><span class="highlight">PLATZ</span> für<br>Neues!</h1>

    <p class="web">www.brenholt-bau.com</p>

    <ul class="services" style="list-style:none">
      <li class="service">Industrierückbau</li>
      <li class="service">Abbruch &amp; Entkernen</li>
      <li class="service">Entsorgung</li>
      <li class="service">Schadstoffsanierung<br>Asbest, KMF, PAK</li>
    </ul>
  </main>
</body>
</html>
```